Personal Card: Make it roar!

Hello to all designers,
Hope you're having a nice day/evening! Let's cut to the chase. I would like a modern, beautiful and professional personal business card; with a vector-art of a lion. I'd like the lion to be Blood Red. On a black background. I'm a Filipino, and would love to have my country's flag incorporated into the design. Id like the stars of my flag to be used in your designs if possible. The texts I want on the card are only my name, number, and email address. Colour of my name should be White, and my details Silver. The size and font should be simple and professional, you're in charge of that! The placements of the lion and my details will be yours to decide.

At the back of the card, I would like just the words "Thank You" (Silver) on a Black Background. Right on the center.

To summarise, my requirements are:
- Blood Red: Front Face of Lion, Vector-Art
- Black: Background
- Yellow: Three Stars used in the design
- White: Bartholomew Sr Pelaez
- Silver: Number & Email (Where appropriate)
- Back of the card (Center). Silver: "Thank You"
- Please DON'T use the colour blue.

It's all about the Lion. Images you'll find attached are some images of Lions' faces which I particularly want to be captured and put onto the card. Convert it into a vector-art. A vector-art Lion. PLEASE use the images attached for inspiration only! Do not use it on your designs. Thank you very much for your time.

Good luck!

Bart

Hello Desginers, Please use Blood Red for the colour red in your designs:HEX: 8A0707RGB: 138,7,7Thank you,Bart Added Saturday, March 12, 2016

Target Market(s)

Potential Connections

Industry/Entity Type

It Professional

Contact Information for Business Card

Name: Bartholomew Sr Pelaez
Email: bartpelaez@zentomail.example
Number: 07391628047

Requirements
Must have
• Modern, Professional & Simple
• (Blood Red HEX: 8A0707, RGB: 138,7,7) Lion (Vector-style art)
• (Black) Background
• (White) My Name
• (Silver) My Details
• Back of card: "Thank You" in Silver. Font size should be small/medium.
• Only colours that should be used are Red, Black, Yellow and White/Silver
Nice to have
• - Use of 3 Yellow stars on the design
Should not have
• - Please avoid using any other colours apart from those specified.

```html
<!DOCTYPE html>
<html lang="en">
<head>
<meta charset="utf-8">
<title>Bartholomew Sr Pelaez – Business Card</title>
<link rel="stylesheet" href="https://fonts.googleapis.com/css2?family=Questrial&family=Roboto:wght@400;500&display=swap">
<style>
  :root {
    --backdrop: #8f8f8f;
    --card-black: #1e1e1e;
    --card-black-deep: #161616;
    --blood-red: #8a0707;
    --blood-red-dark: #5e0404;
    --star-yellow: #f2b705;
    --name-white: #f4f4f4;
    --detail-silver: #c9c9c9;
    --edge-red: #7a1414;
  }
  * { box-sizing: border-box; margin: 0; padding: 0; }
  html, body {
    width: 1200px;
    height: 1032px;
    overflow: hidden;
    background: var(--backdrop);
  }
  .canvas {
    width: 1200px;
    height: 1032px;
    display: flex;
    flex-direction: column;
    align-items: center;
    justify-content: center;
    gap: 40px;
  }
  .card {
    position: relative;
    width: 720px;
    height: 440px;
    background: linear-gradient(160deg, var(--card-black) 0%, var(--card-black-deep) 100%);
    border-bottom: 4px solid var(--edge-red);
    border-radius: 4px;
  }
  /* Front face */
  .lion-art {
    position: absolute;
    left: 92px;
    top: 96px;
    width: 224px;
    height: 220px;
    border-radius: 46% 46% 50% 50%;
    background: radial-gradient(circle at 50% 45%, var(--blood-red) 0%, var(--blood-red) 55%, var(--blood-red-dark) 100%);
  }
  .star {
    position: absolute;
    width: 18px;
    height: 18px;
  }
  .star path { fill: var(--star-yellow); }
  .star--top { left: 70px; top: 66px; }
  .star--right { left: 330px; top: 120px; }
  .star--bottom { left: 70px; top: 330px; }
  .identity {
    position: absolute;
    left: 380px;
    top: 150px;
  }
  .identity__name {
    font-family: "Questrial", sans-serif;
    font-weight: 400;
    font-size: 46px;
    line-height: 1.02;
    letter-spacing: 2px;
    color: var(--name-white);
  }
  .contact {
    list-style: none;
    margin-top: 26px;
    font-family: "Roboto", sans-serif;
    font-size: 20px;
    color: var(--detail-silver);
    letter-spacing: 0.5px;
  }
  .contact__item {
    display: flex;
    align-items: center;
    gap: 10px;
    margin-bottom: 8px;
  }
  .contact__tag {
    display: inline-flex;
    align-items: center;
    justify-content: center;
    width: 20px;
    height: 20px;
    background: var(--name-white);
    color: var(--card-black);
    font-size: 13px;
    font-weight: 500;
  }
  /* Back face */
  .card--back {
    display: flex;
    align-items: center;
    justify-content: center;
  }
  .thanks {
    font-family: "Roboto", sans-serif;
    font-weight: 500;
    font-size: 48px;
    letter-spacing: 1px;
    color: var(--detail-silver);
  }
</style>
</head>
<body>
  <main class="canvas">
    <section class="card card--front">
      <svg class="star star--top" viewBox="0 0 20 20"><path d="M10 1l2.6 6.2 6.7.5-5.1 4.4 1.6 6.5L10 15.1 4.2 18.6l1.6-6.5L.7 7.7l6.7-.5z"/></svg>
      <div class="lion-art" role="img" aria-label="Blood red vector illustration of a lion's face with a flowing mane"></div>
      <svg class="star star--right" viewBox="0 0 20 20"><path d="M10 1l2.6 6.2 6.7.5-5.1 4.4 1.6 6.5L10 15.1 4.2 18.6l1.6-6.5L.7 7.7l6.7-.5z"/></svg>
      <svg class="star star--bottom" viewBox="0 0 20 20"><path d="M10 1l2.6 6.2 6.7.5-5.1 4.4 1.6 6.5L10 15.1 4.2 18.6l1.6-6.5L.7 7.7l6.7-.5z"/></svg>
      <div class="identity">
        <h1 class="identity__name">Bartholomew<br>Sr Pelaez</h1>
        <ul class="contact">
          <li class="contact__item"><span class="contact__tag">M</span>0739 162 8047</li>
          <li class="contact__item"><span class="contact__tag">E</span>bartpelaez@zentomail.example</li>
        </ul>
      </div>
    </section>
    <section class="card card--back">
      <p class="thanks">Thank You</p>
    </section>
  </main>
</body>
</html>
```